依頼詳細
コーポレートカラーがオレンジなので、オレンジをベースにデザインをお願いしたいと思っております。
見やすさ、内容の伝わりやすさ、先進的なイメージを与えつつ、信頼できる雰囲気のチラシデザインだと嬉しいです。
イメージ画像や写真などは独自にご提案いただいて構いません。
よろしくお願い致します。
記載項目
素案のファイルを添付します
サイズ
A4
ページ数
両面
希望イメージ
シンプル 複雑
単色 カラフル
暗い 明るい
日常 高級
遊び心 厳粛
未来的 伝統的
女性的 男性的
希望する色
黄・オレンジ系
納品ファイル
• 高解像度JPG (.jpg)
• イラストレーター形式 (.ai)
• フォトショップ形式 (.psd)
• PNG形式 (.png)
補足説明

伝わりやすいデザインで、独自のキャッチコピー提案がありました。裏面も見やすい形でデザインしていただけてとてもよかったです。ありがとうございました。

この度はお忙しい中、ご提案いただきましてありがとうございました。
また機会がございましたら、ご提案いただけますと幸いです。

```html
<!DOCTYPE html>
<html lang="ja">
<head>
<meta charset="UTF-8">
<title>AI業務自動化ソリューション</title>
<link href="https://fonts.googleapis.com/css2?family=Noto+Sans+JP:wght@400;500;700;900&family=Oswald:wght@500;600&display=swap" rel="stylesheet">
<style>
  :root{
    --orange:#f29a1f;
    --orange-deep:#c9620a;
    --orange-dark:#6b2e05;
    --ink:#141414;
    --white:#ffffff;
    --cream:#fff8ee;
    --text-soft:#8a4a10;
  }
  *{margin:0;padding:0;box-sizing:border-box;}
  html,body{width:853px;height:1200px;overflow:hidden;background:var(--orange);}
  body{font-family:"Noto Sans JP",sans-serif;color:var(--ink);}
  .flyer{position:relative;width:853px;height:1200px;background:linear-gradient(180deg,var(--orange) 0%,#f5a53a 100%);overflow:hidden;}

  .hero{position:absolute;left:0;top:0;width:853px;height:470px;
    background:radial-gradient(ellipse at 50% 48%,#f0b060 0%,#d97a1c 28%,#9b4610 60%,var(--orange-dark) 100%);}
  .hero-title{position:absolute;left:0;right:0;top:14px;text-align:center;color:var(--white);
    font-weight:500;font-size:44px;letter-spacing:3px;}
  .hero-rule{position:absolute;left:40px;right:40px;top:78px;height:2px;background:rgba(255,255,255,.85);}
  .hero-lead{position:absolute;left:0;right:0;top:406px;text-align:center;color:var(--white);
    font-size:13px;line-height:23px;letter-spacing:.5px;}

  .section-head{position:absolute;left:32px;top:488px;display:flex;align-items:baseline;gap:10px;color:var(--white);}
  .section-num{font-family:"Oswald",sans-serif;font-weight:600;font-size:52px;color:var(--ink);}
  .section-name{font-size:44px;font-weight:500;}
  .brand{position:absolute;right:34px;top:504px;color:var(--white);font-family:"Noto Sans JP",sans-serif;
    font-weight:500;font-size:20px;letter-spacing:1px;}

  .catch{position:absolute;left:28px;right:28px;top:566px;height:40px;background:var(--ink);color:var(--white);
    font-size:24px;font-weight:500;line-height:40px;padding-left:48px;letter-spacing:1px;}
  .points{position:absolute;left:60px;top:622px;list-style:none;color:var(--ink);font-size:13.5px;line-height:23px;}
  .points li::before{content:"・";}

  .feature{position:absolute;left:28px;width:800px;height:118px;}
  .feature-card{position:absolute;left:86px;top:18px;right:0;height:86px;background:var(--cream);
    border-radius:6px;padding:12px 20px 0 72px;}
  .feature-badge{position:absolute;left:0;top:0;width:118px;height:118px;border-radius:50%;background:var(--ink);
    color:var(--white);text-align:center;border:4px solid var(--orange);}
  .badge-label{display:block;font-size:15px;font-weight:700;margin-top:14px;}
  .badge-num{display:block;font-family:"Oswald",sans-serif;font-size:54px;line-height:56px;font-weight:600;}
  .feature-title{font-size:28px;font-weight:700;color:var(--ink);line-height:36px;}
  .feature-text{font-size:13.5px;color:var(--text-soft);line-height:21px;margin-top:4px;}
  .f1{top:694px;} .f2{top:840px;} .f3{top:988px;}
</style>
</head>
<body>
<div class="flyer">
  <div class="hero" role="img" aria-label="Glowing digital brain with large AI letters, surrounded by white line icons for cloud, people, mail, charts and signals"></div>
  <h1 class="hero-title">AI 業務自動化ソリューション</h1>
  <div class="hero-rule"></div>
  <p class="hero-lead">AIによって業務を効率化・自動化し、お客さまのパフォーマンス最大化を支援します。<br>最適なデバイスの選定、ソフト・ハードの設置、テスト、PDCAサイクルまでトータルに導入をサポートします。</p>

  <div class="section-head"><span class="section-num">01.</span><span class="section-name">AI-動画解析</span></div>
  <div class="brand">Nexora</div>

  <div class="catch">ヒト・モノ・コトの特徴をリアルタイムに検出</div>
  <ul class="points">
    <li>人物の属性情報の判別、製造・物流現場での不良品の検出、危険エリアへの侵入検知</li>
    <li>人の目に頼っていた作業の自動化や、業務効率化、安全対策の実施を可能にします。</li>
  </ul>

  <section class="feature f1">
    <div class="feature-card">
      <h2 class="feature-title">業務効率化支援</h2>
      <p class="feature-text">AI画像認識ノウハウと効果的な学習を組み合わせることにより、高精度の認識を実現します。</p>
    </div>
    <div class="feature-badge"><span class="badge-label">特徴</span><span class="badge-num">1</span></div>
  </section>

  <section class="feature f2">
    <div class="feature-card">
      <h2 class="feature-title">高精度の認識率</h2>
      <p class="feature-text">お客さまの業務の現状をしっかりと把握し、最適な改善策をご提案。プロセス全体での改善を図ります。</p>
    </div>
    <div class="feature-badge"><span class="badge-label">特徴</span><span class="badge-num">2</span></div>
  </section>

  <section class="feature f3">
    <div class="feature-card">
      <h2 class="feature-title">解析＋アルファ</h2>
      <p class="feature-text">解析するだけでなく、データの可視化・分析、デバイスへの通知等、柔軟に対応いたします。</p>
    </div>
    <div class="feature-badge"><span class="badge-label">特徴</span><span class="badge-num">3</span></div>
  </section>
</div>
</body>
</html>
```